Freelancers in the field of IT security and IT service need a business card design

I need a business card design for my company. I am a freelancer and active in the area of IT security, IT support% 26 # 252; tung, consulting. I am not yet color-coded, but it should be a modern color that can also be used for a later website. The design should be innovation. Exude dynamism and reliability

Target Market(s)

IT security, IT solutions

Contact Information for Business Card

Firma: brunov-consulting, Inhaber: Lukas Brunov
Adresse: Lindenhof 4, D-73618 Kirchhalden
Telefon: +49 (0) 5137 640928
E-Mail Lukas.Brunov@brunov-consulting.example

```html
<!DOCTYPE html>
<html lang="de">
<head>
<meta charset="utf-8">
<title>brunov-consulting – Visitenkarte</title>
<link rel="stylesheet" href="https://fonts.googleapis.com/css2?family=Roboto:wght@400;500&display=swap">
<style>
  :root {
    --brand-blue: #0b4a80;
    --ink: #2b2b2b;
    --paper: #ffffff;
    --backdrop: #efeff0;
  }
  * { box-sizing: border-box; margin: 0; padding: 0; }
  html, body {
    width: 1200px; height: 800px; overflow: hidden;
    background: var(--backdrop);
    font-family: "Roboto", Arial, sans-serif;
  }
  .canvas { position: relative; width: 1200px; height: 800px; }

  .card { position: absolute; width: 570px; height: 328px; }

  .company-name {
    display: flex; align-items: center; gap: 10px;
    font-weight: 500; line-height: 1; white-space: nowrap;
  }
  .company-name__square { display: block; flex: none; }

  /* Contact side */
  .card--contact { left: 474px; top: 32px; background: var(--paper); }
  .card--contact .company-name {
    position: absolute; right: 42px; top: 52px;
    font-size: 24px; color: var(--brand-blue);
  }
  .card--contact .company-name__square { width: 14px; height: 14px; background: var(--brand-blue); }

  .accent-bar {
    position: absolute; left: 0; top: 180px;
    width: 13px; height: 31px; background: var(--brand-blue);
  }
  .person { position: absolute; left: 43px; top: 170px; }
  .person__name {
    font-size: 19px; font-weight: 500; color: var(--brand-blue);
    text-transform: uppercase; letter-spacing: 0.01em; line-height: 1.1;
  }
  .person__role { font-size: 14px; color: var(--ink); margin-top: 2px; }

  .contact-list {
    position: absolute; left: 43px; top: 230px;
    list-style: none; font-size: 14px; color: var(--ink);
  }
  .contact-list li { display: flex; align-items: center; height: 19.5px; white-space: nowrap; }
  .contact-list__label { color: var(--brand-blue); }
  .contact-list svg { width: 12px; height: 10px; margin-right: 5px; fill: var(--brand-blue); }

  /* Brand side */
  .card--brand {
    left: 168px; top: 404px; background: var(--brand-blue);
    display: flex; align-items: center; justify-content: center;
  }
  .card--brand .company-name { font-size: 30px; color: var(--paper); }
  .card--brand .company-name__square { width: 17px; height: 17px; background: var(--paper); }
</style>
</head>
<body>
<main class="canvas">

  <section class="card card--contact" aria-label="Visitenkarte Vorderseite">
    <p class="company-name"><span class="company-name__square"></span>brunov-consulting</p>

    <div class="accent-bar"></div>
    <div class="person">
      <p class="person__name">Lukas Brunov</p>
      <p class="person__role">Director</p>
    </div>

    <ul class="contact-list">
      <li><span class="contact-list__label">Adresse:</span>&nbsp;Lindenhof 4, D-73618 Kirchhalden</li>
      <li>
        <svg viewBox="0 0 12 10" aria-hidden="true"><path d="M1 3.2C1 1.8 3 1 6 1s5 .8 5 2.2V4H8.6V3.1H3.4V4H1zM3 4.6h6l2 2.2V9H1V6.8zM6 5.8a1.3 1.3 0 1 0 0 2.6 1.3 1.3 0 0 0 0-2.6z"/></svg>
        +49 (0) 5137 640928
      </li>
      <li>
        <svg viewBox="0 0 12 10" aria-hidden="true"><path d="M0 1h12v1.2L6 5.6 0 2.2zM0 3.4l6 3.4 6-3.4V9H0z"/></svg>
        Lukas.Brunov@brunov-consulting.example
      </li>
    </ul>
  </section>

  <section class="card card--brand" aria-label="Visitenkarte Rückseite">
    <p class="company-name"><span class="company-name__square"></span>brunov-consulting</p>
  </section>

</main>
</body>
</html>
```